Business Card 85x40mm - Freelance audio mixing / live event operator

I am a freelance audio operator working in live events. Mostly corporate events mixing sound for a range of entertainment, awards nights and functions. I need a new card to give to perspective clients.

The final design will convey bold professionalism with a general dark vibe. Looking for dark-ish background with some smatterings of colour added.

I have attatched my old BC for an idea of what I have liked in the past. Id like a more modern updated design (that circular design on the back is not my logo it is just a picture I found that resembled sound} . For an added element possibly a mixture of some playful colours in a way that resembles an audio wave form or sound.

I have attached a photo called "audio software" with some colourful squiggly lines; maybe incorporate elements of that into into design
Updates

Added extra $ to project Damn Pixel hives fees are unreasonable

Target Market(s)

Mostly corporate clients

Industry/Entity Type

Events

Contact Information for Business Card

Corwin Pellath
Sound | FOH | Monitors | Systems | Corporate

Digital Audio Mixing Specialist, Live Event Technical Professional,

corwinpellath@mailvexo.net, +61 402 918 357

Colors
ec1f27
ffc214
9bcb3c
6b449b

Requirements
Must have
• Dark theme
• 85x40mm dimensions
Nice to have
• some sort of imagery or design to reflect audio/sound

```html
<!DOCTYPE html>
<html lang="en">
<head>
<meta charset="utf-8">
<title>Corwin Pellath — Business Card</title>
<link rel="stylesheet" href="https://fonts.googleapis.com/css2?family=Tinos&family=Arimo&family=Russo+One&display=swap">
<style>
  :root {
    --page: #ffffff;
    --card: #0a0c0b;
    --card-back: #121416;
    --ink: #ffffff;
    --band: #6e2c45;
    --wave-pink: #8a3a62;
    --wave-blue: #2a3e6e;
    --wave-teal: #1d6a5a;
  }
  html, body {
    margin: 0;
    padding: 0;
    width: 1167px;
    height: 1200px;
    overflow: hidden;
    background: var(--page);
  }
  .sheet {
    position: relative;
    width: 1167px;
    height: 1200px;
  }
  .card {
    position: absolute;
    left: 110px;
    width: 996px;
    height: 471px;
    overflow: hidden;
  }
  .card--front { top: 130px; background: var(--card); }
  .card--back  { top: 667px; background: var(--card-back); }

  .waveform {
    position: absolute;
    left: 0;
    top: 60px;
    width: 600px;
    height: 202px;
    background:
      linear-gradient(to bottom,
        transparent 0%,
        rgba(29,106,90,0.55) 8%,
        rgba(42,62,110,0.7) 25%,
        rgba(138,58,98,0.75) 42%,
        rgba(138,58,98,0.85) 50%,
        rgba(138,58,98,0.75) 58%,
        rgba(42,62,110,0.7) 75%,
        rgba(29,106,90,0.55) 92%,
        transparent 100%);
    -webkit-mask: radial-gradient(ellipse 70% 60% at 50% 50%, #000 60%, transparent 100%);
            mask: radial-gradient(ellipse 70% 60% at 50% 50%, #000 60%, transparent 100%);
  }
  .name-band {
    position: absolute;
    left: 600px;
    top: 156px;
    width: 396px;
    height: 11px;
    background: var(--band);
  }
  .name {
    position: absolute;
    left: 611px;
    top: 112px;
    margin: 0;
    font-family: "Tinos", "Times New Roman", serif;
    font-weight: 400;
    font-size: 45px;
    letter-spacing: 1px;
    color: var(--ink);
    line-height: 1;
  }
  .services {
    position: absolute;
    left: 0;
    width: 996px;
    top: 270px;
    margin: 0;
    text-align: center;
    font-family: "Arimo", Arial, sans-serif;
    font-size: 23px;
    color: var(--ink);
    transform: translateX(-6px);
  }
  .contact {
    position: absolute;
    top: 352px;
    left: 198px;
    display: flex;
    align-items: center;
    gap: 0;
    font-family: "Arimo", Arial, sans-serif;
    font-size: 23px;
    color: var(--ink);
  }
  .contact__item { display: flex; align-items: center; }
  .contact__item + .contact__item { margin-left: 26px; }
  .contact__icon { width: 24px; height: 24px; margin-right: 16px; fill: var(--ink); }

  .console-photo {
    position: absolute;
    inset: 0;
    background:
      radial-gradient(ellipse 60% 50% at 40% 30%, #1c2022 0%, transparent 70%),
      linear-gradient(170deg, #181b1d 0%, #0f1112 60%, #151719 100%);
  }
  .tagline {
    position: absolute;
    left: 0;
    width: 996px;
    top: 148px;
    margin: 0;
    text-align: center;
    font-family: "Russo One", Impact, sans-serif;
    font-size: 33px;
    line-height: 38px;
    color: var(--ink);
    transform: skewX(-12deg);
    letter-spacing: -0.5px;
  }
  .back-rule {
    position: absolute;
    left: 3px;
    right: 0;
    top: 243px;
    height: 3px;
    background: var(--ink);
  }
</style>
</head>
<body>
<main class="sheet">
  <section class="card card--front">
    <div class="waveform" role="img" aria-label="Pixel-style audio waveform in teal, blue and magenta"></div>
    <div class="name-band"></div>
    <h1 class="name">Corwin Pellath</h1>
    <p class="services">Sound&nbsp; |&nbsp; FOH&nbsp; |&nbsp; Monitors&nbsp; |&nbsp; Systems&nbsp; |&nbsp; Corporate</p>
    <div class="contact">
      <span class="contact__item">
        <svg class="contact__icon" viewBox="0 0 24 24" aria-hidden="true"><path d="M1 6h22v13H1z M2.5 7.5 12 14l9.5-6.5" fill="none" stroke="#fff" stroke-width="2"/><path d="M1 6h22L12 13.5z"/></svg>
        corwinpellath@mailvexo.net
      </span>
      <span class="contact__item">
        <svg class="contact__icon" viewBox="0 0 24 24" aria-hidden="true"><path d="M6.6 10.8c1.4 2.8 3.8 5.1 6.6 6.6l2.2-2.2c.3-.3.7-.4 1-.2 1.1.4 2.3.6 3.6.6.6 0 1 .4 1 1V20c0 .6-.4 1-1 1C10.6 21 3 13.4 3 4c0-.6.4-1 1-1h3.5c.6 0 1 .4 1 1 0 1.3.2 2.5.6 3.6.1.3 0 .7-.2 1z"/></svg>
        +61 402 918 357
      </span>
    </div>
  </section>

  <section class="card card--back">
    <div class="console-photo" role="img" aria-label="Dark close-up photo of a mixing console with faders and knobs"></div>
    <p class="tagline">Digital Audio Mixing Specialist,<br>Live Event Technical Professional,</p>
    <div class="back-rule"></div>
  </section>
</main>
</body>
</html>
```